Accounting Practice Business Card Design

I have a logo I am happy for you to use in the design of the Business Card.
You can edit and change colours as you please, I am not fixated on it.
I am looking for a modern and clean overall feel for the finished design.

The business is a small accounting practice who thrives on word of mouth referrals and this card will be given to all current and prospect clients.

Industry/Entity Type

Accountant

Contact Information for Business Card

Marcus Elwin
Level 5, 8 Corvale Ridge Road
ASHGROVE RISE VIC 3187
Phone: 9481 3057
Email: melwin@mrfaccountants.com.au
Web: www.mrfaccountants.com.au

Font styles to use
Serif
Sans Serif

Colors
0555a3
3277b5
85acd3
0393ce
33a6d7
85cae6
00a990
33b8a4
9bcb3c

Requirements
Must have
• "The end to your tax problems begin with us"
• "A referral from you is our greatest compliment"
Nice to have
• Modern clean professional

```html
<!DOCTYPE html>
<html lang="en">
<head>
<meta charset="utf-8">
<title>MRF Accountants – Business Card</title>
<link rel="stylesheet" href="https://fonts.googleapis.com/css2?family=Michroma&display=swap">
<style>
  :root {
    --page: #e9ebee;
    --card-dark: #232323;
    --card-light: #ffffff;
    --brand-blue: #0555a3;
    --navy: #2b3384;
    --green: #3a8a3a;
    --muted: #4a4a4a;
    --white: #ffffff;
  }
  * { box-sizing: border-box; margin: 0; padding: 0; }
  html, body { width: 1200px; height: 900px; overflow: hidden; }
  body {
    background: var(--page);
    font-family: "Michroma", "Arial", sans-serif;
    position: relative;
  }
  .card {
    position: absolute;
    left: 250px;
    width: 700px;
    height: 400px;
    border-radius: 18px;
    overflow: hidden;
    box-shadow: 0 10px 30px rgba(0,0,0,.18);
  }
  .card--front { top: 30px; background: var(--card-dark); }
  .card--back { top: 470px; background: var(--card-light); }

  /* brand name */
  .brand {
    display: flex;
    align-items: center;
    gap: 14px;
    color: var(--brand-blue);
  }
  .brand__mark { width: 18px; height: 18px; background: var(--green); }
  .brand__name { font-size: 30px; letter-spacing: 1px; }

  .card--front .brand {
    position: absolute;
    top: 96px;
    left: 0; right: 0;
    justify-content: center;
  }
  .card--front .brand__name { font-size: 38px; color: #3277b5; }

  .band {
    position: absolute;
    left: 0; right: 0;
    height: 70px;
    display: flex;
    align-items: center;
    justify-content: center;
    color: var(--white);
    font-size: 15.5px;
    letter-spacing: .5px;
    text-transform: uppercase;
  }
  .band--referral { top: 260px; background: var(--green); }
  .band--promise { top: 330px; background: var(--navy); }

  /* back */
  .card--back .brand { position: absolute; top: 56px; right: 46px; }
  .card--back .brand__name { font-size: 24px; }

  .person { position: absolute; top: 140px; left: 46px; }
  .person__name { color: var(--navy); font-size: 19px; text-transform: uppercase; }
  .person__title { color: var(--muted); font-size: 11.5px; margin-top: 8px; }

  .contact {
    position: absolute;
    left: 46px;
    bottom: 46px;
    list-style: none;
    color: var(--muted);
    font-size: 11.5px;
  }
  .contact__item { display: flex; align-items: center; gap: 12px; margin-top: 10px; }
  .contact__icon { width: 16px; height: 16px; fill: var(--navy); }
  .contact__web { color: var(--navy); font-size: 13.5px; margin-top: 12px; }

  .address {
    position: absolute;
    right: 46px;
    bottom: 56px;
    text-align: right;
    color: var(--navy);
    font-size: 12px;
    line-height: 1.8;
    font-style: normal;
  }
  .address__line--caps { text-transform: uppercase; }

  .edge-stripe {
    position: absolute;
    left: 0; right: 0; bottom: 0;
    height: 9px;
    display: flex;
  }
  .edge-stripe__navy { flex: 0 0 72%; background: var(--navy); }
  .edge-stripe__green { flex: 1; background: var(--green); }
</style>
</head>
<body>

<section class="card card--front" aria-label="Card front">
  <div class="brand">
    <span class="brand__mark"></span>
    <span class="brand__name">MRF ACCOUNTANTS</span>
  </div>
  <div class="band band--referral">A referral from you is our greatest compliment</div>
  <div class="band band--promise">The end to your tax problems begin with us</div>
</section>

<section class="card card--back" aria-label="Card back">
  <div class="brand">
    <span class="brand__mark"></span>
    <span class="brand__name">MRF ACCOUNTANTS</span>
  </div>

  <div class="person">
    <p class="person__name">Marcus Elwin</p>
    <p class="person__title">Managing Director</p>
  </div>

  <ul class="contact">
    <li class="contact__item">
      <svg class="contact__icon" viewBox="0 0 24 24" aria-hidden="true"><path d="M6.6 10.8a15.1 15.1 0 0 0 6.6 6.6l2.2-2.2a1 1 0 0 1 1-.25 11.4 11.4 0 0 0 3.6.57 1 1 0 0 1 1 1V20a1 1 0 0 1-1 1A17 17 0 0 1 3 4a1 1 0 0 1 1-1h3.5a1 1 0 0 1 1 1c0 1.25.2 2.45.57 3.57a1 1 0 0 1-.25 1z"/></svg>
      <span>9481 3057</span>
    </li>
    <li class="contact__item">
      <svg class="contact__icon" viewBox="0 0 24 24" aria-hidden="true"><path d="M2 5h20v14H2z M4 7v.4l8 5.2 8-5.2V7z" fill-rule="evenodd"/></svg>
      <span>melwin@mrfaccountants.com.au</span>
    </li>
    <li class="contact__item contact__web">www.mrfaccountants.com.au</li>
  </ul>

  <address class="address">
    <span class="address__line">Level 5, 8 Corvale Ridge Road</span><br>
    <span class="address__line address__line--caps">Ashgrove Rise VIC 3187</span>
  </address>

  <div class="edge-stripe">
    <span class="edge-stripe__navy"></span>
    <span class="edge-stripe__green"></span>
  </div>
</section>

</body>
</html>
```